Email Signature & Friendbook Cover Design – Brightpath Learning Nook

I’m looking for a clean, professional email signature and a matching Friendbook cover photo for my tutoring business, Brightpath Learning Nook.
The email signature needs to display properly across Outlook and iPhone without the image appearing as an attachment. It should include my logo and contact details and have a friendly but professional look suitable for an education business.
Details to include:
Dana Morrow
Director & Lead Tutor
Brightpath Learning Nook
hello@brightpathlearningnook.co.uk
www.brightpathlearningnook.co.uk
01632 960418
The Friendbook cover should match the branding, feel professional and welcoming, and be optimised for desktop and mobile.

```html
<!DOCTYPE html>
<html lang="en">
<head>
<meta charset="utf-8">
<title>Brightpath Learning Nook – Email Signature</title>
<link rel="stylesheet" href="https://fonts.googleapis.com/css2?family=Raleway:wght@500;600;700&family=Rubik:wght@500&display=swap">
<style>
  :root {
    --green: #40b773;
    --white: #ffffff;
    --rule: rgba(255,255,255,0.28);
    --shade: rgba(0,0,0,0.035);
    --glow: rgba(255,255,255,0.045);
  }
  * { margin: 0; padding: 0; box-sizing: border-box; }
  html, body {
    width: 1200px; height: 1200px; overflow: hidden;
    background: var(--green);
  }
  .signature {
    position: relative;
    width: 1200px; height: 1200px;
    background: var(--green);
    color: var(--white);
    font-family: "Raleway", sans-serif;
    overflow: hidden;
  }
  .backdrop { position: absolute; inset: 0; }
  .brand-name {
    position: absolute; right: 42px; top: 100px;
    text-align: right;
    font-weight: 700; font-size: 64px; line-height: 1.05;
    color: var(--white);
  }
  .person {
    position: absolute; left: 52px; top: 525px;
    display: flex; align-items: baseline; gap: 24px;
    white-space: nowrap;
  }
  .person-name {
    font-family: "Rubik", sans-serif; font-weight: 500; font-size: 53px;
  }
  .person-role { font-weight: 600; font-size: 42px; }
  .rule {
    position: absolute; left: 52px; width: 984px; height: 1px;
    background: var(--rule);
  }
  .rule-top { top: 655px; }
  .rule-bottom { top: 982px; }
  .contact-list { position: absolute; left: 52px; top: 690px; list-style: none; }
  .contact-item {
    display: flex; align-items: baseline; height: 91px;
    font-size: 35px; font-weight: 500;
  }
  .contact-label { width: 64px; font-size: 36px; font-weight: 500; }
  .social-row {
    position: absolute; left: 0; top: 1034px; width: 1200px; height: 56px;
  }
  .social-link {
    position: absolute; top: 0; display: flex; align-items: center; gap: 16px;
    font-size: 34px; font-weight: 500; white-space: nowrap;
  }
  .social-dot {
    width: 56px; height: 56px; border-radius: 50%;
    border: 2px solid var(--white);
  }
  .social-divider {
    position: absolute; top: 4px; width: 1px; height: 48px; background: var(--rule);
  }
</style>
</head>
<body>
<main class="signature">
  <svg class="backdrop" width="1200" height="1200" viewBox="0 0 1200 1200" aria-hidden="true">
    <path fill="var(--shade)" d="M1200 645 C1080 540 940 470 840 480 C700 495 620 620 625 760 C630 900 720 1040 800 1200 L1200 1200 Z"/>
    <path fill="var(--glow)" d="M105 1200 C80 1060 110 900 230 860 C380 810 620 950 770 1060 L860 1200 Z"/>
  </svg>

  <div class="brand-name">Brightpath<br>Learning<br>Nook</div>

  <div class="person">
    <span class="person-name">Dana Morrow,</span>
    <span class="person-role">Director &amp; Lead Tutor</span>
  </div>

  <div class="rule rule-top"></div>

  <ul class="contact-list">
    <li class="contact-item"><span class="contact-label">M:</span><span>01632 960418</span></li>
    <li class="contact-item"><span class="contact-label">E:</span><span>hello@brightpathlearningnook.co.uk</span></li>
    <li class="contact-item"><span class="contact-label">W:</span><span>www.brightpathlearningnook.co.uk</span></li>
  </ul>

  <div class="rule rule-bottom"></div>

  <nav class="social-row">
    <span class="social-link" style="left:52px"><span class="social-dot"></span>Pathnet</span>
    <span class="social-divider" style="left:300px"></span>
    <span class="social-link" style="left:327px"><span class="social-dot"></span>WorkLink</span>
    <span class="social-divider" style="left:585px"></span>
    <span class="social-link" style="left:629px"><span class="social-dot"></span>Friendbook</span>
    <span class="social-divider" style="left:873px"></span>
    <span class="social-link" style="left:916px"><span class="social-dot"></span>Snapgram</span>
  </nav>
</main>
</body>
</html>
```